Business Card Design Project

We need a business card design for a consultancy called 'Maple Ridge'. The design should communicate innovation and professionalism. The colors used should complement our logo. Please include source files for winning design.
Updates

Industry/Entity Type

Business

Colors

Designer to choose colors to be used in the design.

Requirements
Must have
• Card size should be 85mm x 50mm. The back side of the card should be the logo on a black background. The front side should display the name 'Maple Ridge' along with standard information. The front's design should graphically complement the back.
Nice to have
• Any graphical elements in the front the complement the back side (with the logo on a black background) would be a plus.

```html
<!DOCTYPE html>
<html lang="en">
<head>
<meta charset="utf-8">
<title>Maple Ridge — Business Card</title>
<link rel="stylesheet" href="https://fonts.googleapis.com/css2?family=Cinzel:wght@500&family=Courier+Prime:wght@700&display=swap">
<style>
  :root {
    --backdrop: #cbc6c3;
    --card-black: #0d0b0a;
    --card-black-soft: #1c1a19;
    --gold: #eaa43c;
    --amber: #e0781c;
    --mark: #f0a232;
    --name-font: "Cinzel", serif;
    --info-font: "Courier Prime", monospace;
  }
  html, body {
    margin: 0;
    padding: 0;
    overflow: hidden;
  }
  .stage {
    width: 1200px;
    height: 789px;
    background: var(--backdrop);
    position: relative;
    overflow: hidden;
  }
  .card {
    position: absolute;
    top: 247px;
    width: 500px;
    height: 294px;
    background: linear-gradient(160deg, var(--card-black-soft), var(--card-black) 60%);
    box-shadow: 0 10px 24px rgba(0, 0, 0, 0.25);
    overflow: hidden;
  }
  .card--front { left: 70px; }
  .card--back  { left: 630px; }

  /* Front */
  .brand-block {
    position: absolute;
    left: 40px;
    top: 70px;
    width: 240px;
    text-align: center;
  }
  .brand-dot {
    width: 82px;
    height: 82px;
    border-radius: 50%;
    background: var(--mark);
    margin: 0 auto 14px;
  }
  .brand-name {
    font-family: var(--name-font);
    font-weight: 500;
    font-size: 29px;
    letter-spacing: 1px;
    color: var(--gold);
    margin: 0;
    white-space: nowrap;
  }
  .divider {
    position: absolute;
    left: 298px;
    top: 122px;
    width: 8px;
    height: 80px;
  }
  .contact {
    position: absolute;
    left: 318px;
    top: 130px;
    margin: 0;
    font-family: var(--info-font);
    font-weight: 700;
    font-size: 11.5px;
    line-height: 15px;
    color: var(--amber);
    font-style: normal;
    white-space: nowrap;
  }

  /* Back */
  .back-mark {
    position: absolute;
    left: 50%;
    top: 50%;
    transform: translate(-50%, -50%);
    text-align: center;
  }
  .back-mark .brand-dot {
    width: 150px;
    height: 150px;
    margin-bottom: 16px;
  }
  .back-mark .brand-name {
    font-size: 22px;
  }
</style>
</head>
<body>
<main class="stage">
  <section class="card card--front" aria-label="Front of card">
    <div class="brand-block">
      <div class="brand-dot" aria-hidden="true"></div>
      <h1 class="brand-name">MAPLE RIDGE</h1>
    </div>
    <svg class="divider" viewBox="0 0 8 80" aria-hidden="true">
      <line x1="1" y1="0" x2="1" y2="80" stroke="#e0781c" stroke-width="1.5"/>
      <line x1="6" y1="10" x2="6" y2="70" stroke="#e0781c" stroke-width="1.5"/>
    </svg>
    <address class="contact">
      214 Harbor Rd #12B<br>
      Brookvale, OR 97014<br>
      p. 55 014 226 80<br>
      www.mapleridge.com
    </address>
  </section>

  <section class="card card--back" aria-label="Back of card">
    <div class="back-mark">
      <div class="brand-dot" aria-hidden="true"></div>
      <p class="brand-name">MAPLE RIDGE</p>
    </div>
  </section>
</main>
</body>
</html>
```